Real Estate Sign 2

Our company is called Corwin Hadley Realty. We are a real estate development company. We need a sign that we are going to hang outside of our projects that says: Another project brought to you by Corwin Hadley Realty... For Sale....(213) 555-0187. At the very bottom is needs to say CaBRE# 04637251" We want the Corwin Hadley Realty to be sophisticated, fresh, simple. We do not have a logo so maybe one can be incorporated into the sign. Sign will be about 30"x24"

Industry/Entity Type

Real Estate

```html
<!DOCTYPE html>
<html lang="en">
<head>
<meta charset="utf-8">
<title>Corwin Hadley Realty – For Sale Sign</title>
<link rel="stylesheet" href="https://fonts.googleapis.com/css2?family=EB+Garamond:wght@400&display=swap">
<style>
  :root {
    --sign-bg: #ffffff;
    --ink: #000000;
  }
  html, body {
    margin: 0;
    padding: 0;
    width: 1200px;
    height: 900px;
    overflow: hidden;
    background: var(--sign-bg);
  }
  .sign {
    position: relative;
    width: 1200px;
    height: 900px;
    background: var(--sign-bg);
    color: var(--ink);
    font-family: "EB Garamond", Garamond, serif;
    font-weight: 400;
  }
  .sign > * {
    position: absolute;
    left: 0;
    width: 100%;
    margin: 0;
    text-align: center;
    line-height: 1;
    white-space: nowrap;
  }
  .intro-line {
    top: 49px;
    font-size: 50px;
    padding-left: 8px;
    box-sizing: border-box;
  }
  .company-name {
    top: 183px;
    font-size: 120px;
  }
  .company-name span {
    display: block;
  }
  .company-name .name-second-line {
    margin-top: 20px;
    padding-left: 0;
  }
  .divider {
    top: 477px;
    left: 81px;
    width: 1038px;
    height: 8px;
    background: var(--ink);
  }
  .status {
    top: 500px;
    font-size: 190px;
  }
  .phone {
    top: 686px;
    font-size: 92px;
    padding-left: 8px;
    box-sizing: border-box;
  }
  .license {
    top: 828px;
    font-size: 40px;
  }
</style>
</head>
<body>
  <main class="sign">
    <p class="intro-line">Another project brought to you by</p>
    <h1 class="company-name">
      <span class="name-first-line">Corwin Hadley</span>
      <span class="name-second-line">Realty</span>
    </h1>
    <div class="divider" aria-hidden="true"></div>
    <p class="status">For Sale</p>
    <p class="phone">(213) 555-0187</p>
    <p class="license">CaBRE# 04637251</p>
  </main>
</body>
</html>
```